User Photo Sharing Wordpress Design

We need a wordpress design that is ready launch-ready for our Company called Tarrowmere. We allow users to submit their photos to our site in hopes that they will become the "Photo of the Day." Right now we are just running plug-ins to help with User submission but they do not accomplish our main goal: User submission goes directly to a created post and waits for admin approval of launch. We are specifically looking for a method integrated directly into wordpress that will allow users to submit their images and immediately, it automatically creates a post draft for the website admin to approve or deny. The user-submit area should collect the following data: Photo, Photo Information, First and Last name (or social media tag), Mobile Number, and Email List. We would suggest that the user can login to encourage loyalty and constant use.

This website also needs sufficient advertising space and a blog. We are looking to create something that is easy to replicate in multiple cities.

The final design should be ready to launch and be able to accomplish the main goal (successful photo sharing) at the minimum with a sleek design that is easy to use and is responsive.
Updates

Just as clarification... I am looking for a completed project that I can use on Wordpress ASAP.  This project has to allow my website visitors to upload their images and those images should be automatically loaded into a post and saved as a draft (or some variation of that process), allowing the website admin to approve or deny.  Information collecting is VITAL during the photo submission process.  This site needs to be responsive as well.  

Target Market(s)

Mostly Woman 13-65

Industry/Entity Type

Advertising

Requirements
Must have
• Photo submission methods allowing user to submit photos and admin to approve the created post.

Information collection (Name, Email, Mobile, Photo, Photo Info)
Nice to have
• Blog, photo segmentation, advertising room

```html
<!DOCTYPE html>
<html lang="en">
<head>
<meta charset="utf-8">
<title>Tarrowmere</title>
<link rel="stylesheet" href="https://fonts.googleapis.com/css2?family=Cabin:wght@400;600&family=Open+Sans:wght@400;600&display=swap">
<style>
:root{
  --paper:#efece4;
  --ink:#222;
  --muted:#555;
  --footer:#262626;
  --accent:#e59a12;
  --navdark:#2a2a2a;
  --rule:#cfcac0;
}
*{margin:0;padding:0;box-sizing:border-box}
html,body{width:839px;height:1200px;overflow:hidden}
body{position:relative;background:var(--paper);font-family:"Open Sans",sans-serif;color:var(--ink)}
.abs{position:absolute}
.hero{left:0;top:0;width:839px;height:508px;background:linear-gradient(180deg,#c9ccd0 0%,#8a8f9a 18%,#c4905a 26%,#1c3550 34%,#1f4a78 55%,#173657 75%,#111b26 100%)}
.header{left:0;top:0;width:839px;height:84px;background:rgba(235,236,238,.72)}
.brand{left:60px;top:20px;font-family:"Cabin",sans-serif;font-weight:600;font-size:30px;color:#111;letter-spacing:-.5px;display:flex;align-items:center;gap:8px}
.brand i{width:12px;height:12px;border-radius:50%;background:#111;display:block}
.nav{left:436px;top:39px;display:flex;font-family:"Cabin",sans-serif;font-weight:600;font-size:11px;color:#111}
.nav a{display:block;height:27px;line-height:27px;padding:0 14px;text-decoration:none;color:inherit}
.nav a.active{background:var(--navdark);color:#fff;border-radius:2px}
.caption{left:49px;top:284px;width:366px;height:98px;background:rgba(60,64,72,.72);color:#fff;padding:10px 16px;font-family:"Cabin",sans-serif}
.caption h1{font-weight:400;font-size:19px;margin-bottom:8px}
.caption p{font-size:14px;line-height:22px}
.slider-arrows{left:749px;top:472px;width:29px;height:18px;background:rgba(0,0,0,.45)}
.section-title{left:59px;top:540px;width:721px;height:18px;display:flex;align-items:center;gap:8px;font-family:"Cabin",sans-serif;font-size:13px}
.section-title .line{flex:1;border-top:2px dotted var(--rule)}
.section-title .dot{width:11px;height:11px;border-radius:50%;background:#bdb9b1}
.gallery-item{top:579px;width:168px;height:112px;box-shadow:0 6px 8px -4px rgba(0,0,0,.35)}
.label{font-family:"Cabin",sans-serif;font-size:13px;color:var(--ink)}
.potd-frame{left:49px;top:751px;width:343px;height:205px;background:#fff;box-shadow:0 1px 3px rgba(0,0,0,.2);padding:4px}
.potd-frame div{width:100%;height:100%;background:linear-gradient(180deg,#3e7cc0 0%,#7fa6cf 35%,#2f5a7e 50%,#1d4a7a 62%,#0f2f59 100%)}
.post-thumb{width:86px;border:3px solid #fff;box-shadow:0 1px 3px rgba(0,0,0,.25)}
.post-text{left:512px;width:270px;font-size:9.2px;line-height:18.5px;color:var(--muted)}
.meta{left:519px;display:flex;align-items:center;gap:5px;font-size:9.5px;color:#444}
.meta .count{background:var(--accent);color:#fff;font-size:8px;width:14px;height:13px;text-align:center;line-height:13px}
.meta svg{margin-left:8px}
.divider{left:414px;top:856px;width:366px;border-top:1px dotted var(--rule)}
.ad{top:999px;height:88px}
.footer{left:0;top:1125px;width:839px;height:75px;background:var(--footer);color:#fff}
.copy{left:76px;top:1155px;font-size:9.5px;color:#ddd}
.news-label{left:442px;top:1152px;font-family:"Cabin",sans-serif;font-size:12px;color:#eee}
.news-input{left:507px;top:1149px;width:142px;height:24px;background:#fff;border-radius:2px;color:#999;font-size:14px;text-align:right;padding-right:6px;line-height:23px}
.social{top:1157px;width:9px;height:9px;border-radius:50%;background:#eee}
</style>
</head>
<body>
<div class="abs hero" role="img" aria-label="Dusk seascape with dark rocks in calm blue water and a distant coastline"></div>
<header class="abs header"></header>
<div class="abs brand"><i></i>Tarrowmere</div>
<nav class="abs nav">
  <a class="active" href="#">HOME</a><a href="#">ABOUT US</a><a href="#">BLOG</a><a href="#">PORTFOLIO</a><a href="#">CONTACT</a>
</nav>
<div class="abs caption">
  <h1>Welcome to Tarrowmere</h1>
  <p>Tarrowmere's Only Photo Sharing Website, Featuring Your Photos For Free. Submit Your Photos Now!</p>
</div>
<svg class="abs slider-arrows" viewBox="0 0 29 18"><path d="M10 5l-4 4 4 4M19 5l4 4-4 4" stroke="#fff" stroke-width="1.4" fill="none"/></svg>

<div class="abs section-title"><span class="line"></span><span class="dot"></span>Photo Gallery<span class="dot"></span><span class="line"></span></div>
<div class="abs gallery-item" style="left:60px;background:linear-gradient(180deg,#9fc7e0,#4f8f3a 45%,#7cc83a)" role="img" aria-label="Dandelion in a green meadow"></div>
<div class="abs gallery-item" style="left:243px;background:linear-gradient(180deg,#8fb1a0,#c5b88a 50%,#b86f7e 75%,#6b3f78)" role="img" aria-label="Sunset over the sea"></div>
<div class="abs gallery-item" style="left:426px;background:radial-gradient(circle at 55% 20%,#fff2c0,#d8942e 35%,#6b3a14 100%)" role="img" aria-label="Golden grass backlit by the sun"></div>
<div class="abs gallery-item" style="left:609px;background:linear-gradient(180deg,#6a3010,#f0b040 35%,#8a5a30 60%,#4a4a4a)" role="img" aria-label="Road leading to a city skyline at sunset"></div>

<div class="abs label" style="left:56px;top:727px">Photo of the Day</div>
<div class="abs potd-frame"><div role="img" aria-label="Lake with mountains under a blue sky"></div></div>

<div class="abs label" style="left:414px;top:727px">Blog Posts</div>
<div class="abs post-thumb" style="left:417px;top:758px;height:79px;background:linear-gradient(180deg,#2a4d80,#c98a3a 70%,#222)" role="img" aria-label="City bridge at night"></div>
<p class="abs post-text" style="top:755px">Lorem ipsum dolor sit amet, consectetur adipiscing elit. Sed bla ndit massa vel mauris sollicitudin dignissim. Phasellus ultrices te llus eget.Phasellus ultrices tellus eget mauris.</p>
<div class="abs meta" style="top:824px"><span class="count">5</span>Comments
  <svg width="72" height="11" viewBox="0 0 72 11"><g fill="#f0a21c"><path id="s" d="M5.5 0l1.6 3.6 3.9.4-3 2.6.9 3.9-3.4-2-3.4 2 .9-3.9-3-2.6 3.9-.4z"/><use href="#s" x="15"/><use href="#s" x="30"/></g><g fill="#aaa"><use href="#s" x="45"/><use href="#s" x="60"/></g></svg></div>
<div class="abs divider"></div>
<div class="abs post-thumb" style="left:417px;top:871px;height:78px;background:linear-gradient(180deg,#b8bec4,#6d7884 60%,#3a4654)" role="img" aria-label="Misty city skyscrapers"></div>
<p class="abs post-text" style="top:867px">Lorem ipsum dolor sit amet, consectetur adipiscing elit. Sed bla ndit massa vel mauris sollicitudin dignissim. Phasellus ultrices te llus eget.Phasellus ultrices tellus eget mauris.</p>
<div class="abs meta" style="top:936px"><span class="count">5</span>Comments
  <svg width="72" height="11" viewBox="0 0 72 11"><g fill="#f0a21c"><use href="#s"/><use href="#s" x="15"/><use href="#s" x="30"/></g><g fill="#aaa"><use href="#s" x="45"/><use href="#s" x="60"/></g></svg></div>

<div class="abs ad" style="left:49px;width:351px;background:linear-gradient(90deg,#8a6420,#c89018 50%,#b87a10)" role="img" aria-label="Advertising banner for an energy company"></div>
<div class="abs ad" style="left:411px;width:368px;background:linear-gradient(90deg,#2a5fb8,#4a86d6 60%,#8fb6e6)" role="img" aria-label="Advertising banner for a property security service"></div>

<footer class="abs footer"></footer>
<div class="abs copy">Copyrights 2013. Tarrowmere. All Rights Reserved.</div>
<div class="abs news-label">Newsletter</div>
<div class="abs news-input">»</div>
<span class="abs social" style="left:674px"></span>
<span class="abs social" style="left:699px"></span>
<span class="abs social" style="left:724px"></span>
<span class="abs social" style="left:749px"></span>
</body>
</html>
```